Nine Rung Ledger Remedy Seminar

I would like a flyer to hand out to participants at the speeches that we give. We are a CPA firm that specializes in entrepreneurs and realtors. We would like a flyer that looks crisp and clean, that integrates our logo and our company colors (shades of blue & gold). We would like the wording to be as laid out in the attached documents, but design is up to you. We would like a picture to go along with each point and are open to ideas. The flyer should be one page, preferably just the front.

Colors
3176b5
fee18a

Requirements
Must have
• Our logo and the wording supplied.
• A picture to go along with each topic.
Nice to have
• Images that pop, clean look, professional.
Should not have
• Look messy.

```html
<!DOCTYPE html>
<html lang="en">
<head>
<meta charset="utf-8">
<title>Nine Rung Ledger Remedy Seminar Agenda</title>
<link href="https://fonts.googleapis.com/css2?family=Antonio:wght@200;400&family=Pathway+Gothic+One&family=Roboto+Condensed:wght@700&family=Oswald:wght@700&family=Libre+Baskerville:ital,wght@1,700&family=Open+Sans&display=swap" rel="stylesheet">
<style>
:root{
  --blue:#3176b5;
  --blue-deep:#2a6cae;
  --blue-soft:#8fb6da;
  --gold:#fee18a;
  --gold-pale:#fffcf1;
  --ink:#1b1b1b;
  --white:#ffffff;
}
*{margin:0;padding:0;box-sizing:border-box}
html,body{width:949px;height:1200px;overflow:hidden;background:var(--white)}
.flyer{position:relative;width:949px;height:1200px;background:var(--white)}
.brand{position:absolute;left:45px;top:28px;width:310px}
.brand-name{font-family:"Oswald",sans-serif;font-weight:700;font-size:38px;line-height:1.05;color:var(--blue);letter-spacing:.5px}
.brand-tag{font-family:"Libre Baskerville",serif;font-style:italic;font-weight:700;font-size:13.5px;color:var(--ink);margin-top:46px}
.title{position:absolute;right:59px;top:22px;text-align:right;font-family:"Antonio",sans-serif;font-weight:400;font-size:62px;line-height:82px;color:var(--blue);letter-spacing:1px}
.step{position:absolute;height:104px}
.step.gold{background:linear-gradient(90deg,var(--gold-pale) 0%,#fef3c8 55%,var(--gold) 100%)}
.step.blue{background:linear-gradient(90deg,var(--blue-deep) 0%,#5a92c7 55%,var(--blue-soft) 100%)}
.num{position:absolute;top:8px;font-family:"Antonio",sans-serif;font-weight:200;font-size:80px;line-height:1}
.num::after{content:".";font-weight:400;font-size:40px}
.gold .num{color:var(--blue)}
.blue .num{color:var(--gold)}
.copy{position:absolute;font-family:"Pathway Gothic One",sans-serif;font-size:20px;line-height:25px}
.gold .copy{color:var(--blue)}
.blue .copy{color:var(--gold)}
.copy strong{display:block;font-family:"Roboto Condensed",sans-serif;font-weight:700;font-size:13.5px;line-height:19px}
.copy strong.inline{display:inline}
.gold .copy strong{color:var(--blue-deep)}
.value{position:absolute;display:flex;align-items:center;font-family:"Oswald",sans-serif;font-weight:700;font-size:40px;line-height:1}
.gold .value{color:var(--blue)}
.blue .value{color:var(--gold)}
.value svg{margin-left:4px}
.icon{position:absolute}
.footer{position:absolute;left:59px;top:1120px;width:878px;height:50px;background:linear-gradient(90deg,var(--blue-deep),var(--blue-soft));font-family:"Open Sans",sans-serif;font-size:11.2px;color:var(--gold);text-align:center;padding-top:7px;line-height:19px;word-spacing:1px}
.footer span{margin:0 9px}
</style>
</head>
<body>
<main class="flyer">
  <header>
    <div class="brand">
      <div class="brand-name">TALLYFORD<br>FIGURES</div>
      <div class="brand-tag">A Professional Accounting Corporation</div>
    </div>
    <h1 class="title">Nine Rung Ledger Remedy<br>Seminar Agenda</h1>
  </header>

  <section class="step gold" style="left:20px;top:198px;width:917px">
    <div class="num" style="left:4px">1</div>
    <p class="copy" style="left:71px;top:15px;width:525px">We will first show you how to eliminate much of your self employment tax on your return by converting your business into an S Corporation.<strong>A business owner can make over $120,000 per year can save about $12,000 per year by</strong></p>
    <svg class="icon" style="left:636px;top:12px" width="82" height="82" viewBox="0 0 82 82" fill="none" stroke="var(--blue)" stroke-width="5">
      <circle cx="41" cy="41" r="37"/>
      <line x1="15" y1="67" x2="67" y2="15"/>
      <line x1="41" y1="44" x2="41" y2="14" stroke-width="3"/><polyline points="33,22 41,14 49,22" stroke-width="3"/>
      <text x="41" y="60" text-anchor="middle" font-family="Oswald,sans-serif" font-weight="700" font-size="26" fill="var(--blue)" stroke="none">TAX</text>
    </svg>
    <div class="value" style="left:725px;top:30px">=$$$<svg width="34" height="40" viewBox="0 0 34 40" fill="none" stroke="currentColor" stroke-width="3"><line x1="17" y1="38" x2="17" y2="3"/><polyline points="4,16 17,3 30,16"/></svg></div>
  </section>

  <section class="step blue" style="left:59px;top:326px;width:878px">
    <div class="num" style="left:17px">2</div>
    <svg class="icon" style="left:88px;top:8px" width="92" height="88" viewBox="0 0 92 88" fill="none" stroke="var(--gold)" stroke-width="4.5">
      <polyline points="6,44 46,6 86,44"/><polyline points="18,34 18,84 74,84 74,34"/><rect x="36" y="50" width="20" height="34"/><line x1="66" y1="14" x2="66" y2="28"/>
    </svg>
    <div class="value" style="left:186px;top:32px">=$$$<svg width="34" height="40" viewBox="0 0 34 40" fill="none" stroke="currentColor" stroke-width="3"><line x1="17" y1="38" x2="17" y2="3"/><polyline points="4,16 17,3 30,16"/></svg></div>
    <p class="copy" style="left:352px;top:8px;width:480px">We will show you how to get tax free income from your corporation by renting your home to the corporation for board meeting.<strong>Many of our clients are getting up to $21,000 in tax free income which could put $8,400 cash in your pocket.</strong></p>
  </section>

  <section class="step gold" style="left:20px;top:458px;width:869px">
    <div class="num" style="left:0">3</div>
    <p class="copy" style="left:71px;top:14px;width:550px">We will show you the easiest way to track your expenses so that the only thing you will have to do to have rock solid books is to take a picture of the receipt and throw it away. <strong class="inline">It doesn't get better than that.</strong></p>
    <svg class="icon" style="left:632px;top:8px" width="82" height="94" viewBox="0 0 82 94" fill="none" stroke="var(--blue)" stroke-width="1.6">
      <rect x="2" y="2" width="54" height="72" fill="var(--white)"/>
      <text x="29" y="14" text-anchor="middle" font-family="Pathway Gothic One,sans-serif" font-size="10" fill="var(--blue)" stroke="none">Receipt</text>
      <g stroke-width="1"><line x1="7" y1="24" x2="50" y2="24"/><line x1="7" y1="34" x2="50" y2="34"/><line x1="7" y1="44" x2="50" y2="44"/><line x1="7" y1="54" x2="50" y2="54"/><line x1="7" y1="64" x2="44" y2="64"/></g>
      <rect x="44" y="46" width="24" height="40" rx="3" transform="rotate(22 56 66)" fill="var(--white)" stroke-width="2.5"/>
    </svg>
    <div class="value" style="left:718px;top:32px">=$$$<svg width="34" height="40" viewBox="0 0 34 40" fill="none" stroke="currentColor" stroke-width="3"><line x1="17" y1="38" x2="17" y2="3"/><polyline points="4,16 17,3 30,16"/></svg></div>
  </section>

  <section class="step blue" style="left:59px;top:586px;width:878px">
    <div class="num" style="left:17px">4</div>
    <svg class="icon" style="left:76px;top:16px" width="82" height="74" viewBox="0 0 82 74" fill="none" stroke="var(--gold)" stroke-width="3">
      <rect x="2" y="2" width="78" height="70" rx="4"/>
      <text x="41" y="15" text-anchor="middle" font-family="Oswald,sans-serif" font-weight="700" font-size="12" fill="var(--gold)" stroke="none">PLANNER</text>
      <g stroke-width="1.8"><line x1="2" y1="20" x2="80" y2="20"/><line x1="2" y1="33" x2="80" y2="33"/><line x1="2" y1="46" x2="80" y2="46"/><line x1="2" y1="59" x2="80" y2="59"/><line x1="13" y1="20" x2="13" y2="72"/><line x1="24" y1="20" x2="24" y2="72"/><line x1="35" y1="20" x2="35" y2="72"/><line x1="46" y1="20" x2="46" y2="72"/><line x1="57" y1="20" x2="57" y2="72"/><line x1="68" y1="20" x2="68" y2="72"/></g>
    </svg>
    <div class="value" style="left:165px;top:30px">=$$$<svg width="34" height="40" viewBox="0 0 34 40" fill="none" stroke="currentColor" stroke-width="3"><line x1="17" y1="38" x2="17" y2="3"/><polyline points="4,16 17,3 30,16"/></svg></div>
    <p class="copy" style="left:313px;top:14px;width:520px">Next, We show you the importance of tax planning and why it is critical to meet with your CPA before the end of the year and not just when you do your do your tax preperation.</p>
  </section>

  <section class="step gold" style="left:10px;top:721px;width:879px">
    <div class="num" style="left:8px">5</div>
    <p class="copy" style="left:81px;top:30px;width:545px">We will show you how to hire your children and get $7,500 per child tax free.<strong>This will save you $3,000 per child in income tax reduction.</strong></p>
    <svg class="icon" style="left:635px;top:10px" width="96" height="86" viewBox="0 0 96 86" fill="var(--blue)">
      <circle cx="15" cy="15" r="8"/><rect x="4" y="26" width="22" height="58" rx="6"/>
      <circle cx="48" cy="9" r="8"/><rect x="37" y="20" width="22" height="64" rx="6"/>
      <circle cx="81" cy="15" r="8"/><rect x="70" y="26" width="22" height="58" rx="6"/>
    </svg>
    <div class="value" style="left:733px;top:34px">=$$$<svg width="34" height="40" viewBox="0 0 34 40" fill="none" stroke="currentColor" stroke-width="3"><line x1="17" y1="38" x2="17" y2="3"/><polyline points="4,16 17,3 30,16"/></svg></div>
  </section>

  <section class="step blue" style="left:59px;top:852px;width:878px">
    <div class="num" style="left:17px">6</div>
    <svg class="icon" style="left:75px;top:13px" width="80" height="80" viewBox="0 0 80 80" fill="none" stroke="var(--gold)" stroke-width="4">
      <circle cx="40" cy="40" r="36"/><line x1="15" y1="65" x2="65" y2="15"/>
      <polygon points="14,44 40,34 66,44 40,54" fill="var(--gold)" stroke="none"/><path d="M24 49v10c8 6 24 6 32 0V49" stroke-width="3.5"/>
      <text x="33" y="28" font-family="Oswald,sans-serif" font-weight="700" font-size="14" fill="var(--gold)" stroke="none">$</text>
    </svg>
    <div class="value" style="left:164px;top:30px">=$$$<svg width="34" height="40" viewBox="0 0 34 40" fill="none" stroke="currentColor" stroke-width="3"><line x1="17" y1="38" x2="17" y2="3"/><polyline points="4,16 17,3 30,16"/></svg></div>
    <p class="copy" style="left:313px;top:16px;width:520px">We will discuss how to make your child's college education tax deductible.<strong>With college cost spiraling out of control this is a biggie. Most of our clients have a savings of about $12,000 per year for college.</strong></p>
  </section>

  <section class="step gold" style="left:20px;top:990px;width:869px">
    <div class="num" style="left:0">7</div>
    <p class="copy" style="left:71px;top:14px;width:560px">Our grad finale is to show you how to use,not one but two corporations to get several hundred thousand dollar tax deferral, get a interest free loan from the government and use that money to grow your business and your wealth.</p>
    <svg class="icon" style="left:640px;top:18px" width="84" height="80" viewBox="0 0 84 80" fill="var(--blue)">
      <rect x="8" y="2" width="42" height="76"/><rect x="44" y="30" width="34" height="48"/><rect x="2" y="74" width="80" height="5"/>
      <g fill="var(--gold-pale)"><rect x="13" y="8" width="5" height="5"/><rect x="22" y="8" width="5" height="5"/><rect x="31" y="8" width="5" height="5"/><rect x="13" y="18" width="5" height="5"/><rect x="22" y="18" width="5" height="5"/><rect x="31" y="18" width="5" height="5"/><rect x="13" y="28" width="5" height="5"/><rect x="22" y="28" width="5" height="5"/><rect x="13" y="38" width="5" height="5"/><rect x="22" y="38" width="5" height="5"/><rect x="49" y="38" width="5" height="5"/><rect x="58" y="38" width="5" height="5"/><rect x="67" y="38" width="5" height="5"/><rect x="49" y="48" width="5" height="5"/><rect x="58" y="48" width="5" height="5"/><rect x="67" y="48" width="5" height="5"/><rect x="49" y="58" width="5" height="5"/><rect x="58" y="58" width="5" height="5"/><rect x="20" y="60" width="12" height="14"/></g>
    </svg>
    <div class="value" style="left:728px;top:36px">=$$$<svg width="34" height="40" viewBox="0 0 34 40" fill="none" stroke="currentColor" stroke-width="3"><line x1="17" y1="38" x2="17" y2="3"/><polyline points="4,16 17,3 30,16"/></svg></div>
  </section>

  <footer class="footer">
    <div><span>Tallyford Figures, A professional Accounting Corporation</span><span>www.tallyfordfigurescpa.com</span><span>2718 N. Orchard Ave, Ste. B, Lodeville, CA 95000</span></div>
    <div><span>Phone: 555-014-2277</span><span>Fax: 555-014-2290</span><span>Calder@tallyfordfigurescpas.com</span><span>Wesley@tallyfordfigurescpas.com</span></div>
  </footer>
</main>
</body>
</html>
```